Communications Contractor Business Card Design

I would like a new business card for a new Communications company in Australia. Subcontracting and specialising in cabling, data, phone, antennas, pay tv ,modems, audio visual fibre optics etc. I am open to colour and design concepts but would like a modern clean look that stands out.

Industry/Entity Type

Tv

Contact Information for Business Card

kestrel communications pty ltd, Doug Pemberton, PO BOX 657 Marlow Flats QLD 4873 kestrel4me@maildrop-example.com Australia. ph 0437196084. Director/Technician. services- Cabling,data,phone,antennas,audio visual,home theatre, fibre optics.

```html
<!DOCTYPE html>
<html lang="en">
<head>
<meta charset="utf-8">
<title>Kestrel Communications – Business Card</title>
<link rel="stylesheet" href="https://fonts.googleapis.com/css2?family=Exo+2:wght@300;400;500;600&display=swap">
<style>
  :root {
    --bg: #a9abae;
    --orange: #f26a2b;
    --orange-deep: #ee4a25;
    --amber: #f8a71c;
    --yellow: #fbb617;
    --white: #ffffff;
    --grey-text: #5d5f63;
    --grey-light: #8a8c90;
  }
  * { margin: 0; padding: 0; box-sizing: border-box; }
  html, body { width: 1200px; height: 900px; overflow: hidden; }
  body {
    background: var(--bg);
    font-family: "Exo 2", "Segoe UI", sans-serif;
    display: flex;
    align-items: center;
    justify-content: center;
    gap: 40px;
  }
  .card {
    position: relative;
    width: 540px;
    height: 309px;
    overflow: hidden;
    box-shadow: 0 8px 24px rgba(0,0,0,0.25);
  }

  /* Front (services) side */
  .card-front {
    background: linear-gradient(165deg, var(--orange) 0%, #f37a2a 45%, var(--amber) 80%, var(--yellow) 100%);
    color: var(--white);
  }
  .front-band {
    position: absolute;
    left: 0; right: 0;
    top: 108px;
    height: 84px;
    background: linear-gradient(90deg, rgba(238,74,37,0.15) 0%, rgba(238,74,37,0.75) 55%, var(--orange-deep) 100%);
  }
  .front-watermark {
    position: absolute;
    font-weight: 500;
    font-size: 150px;
    line-height: 1;
    color: rgba(255,255,255,0.1);
    letter-spacing: -2px;
    white-space: nowrap;
  }
  .front-watermark.upper { top: -38px; left: 230px; }
  .front-watermark.lower { top: 150px; left: -30px; color: rgba(238,74,37,0.25); }
  .front-brand {
    position: absolute;
    top: 88px;
    right: 48px;
    text-align: right;
  }
  .brand-name {
    font-weight: 500;
    font-size: 64px;
    line-height: 1;
    letter-spacing: -1px;
  }
  .brand-tagline {
    font-weight: 400;
    font-size: 17px;
    line-height: 1.1;
  }
  .front-brand .brand-tagline { margin-top: 2px; margin-right: 44px; }
  .front-services {
    position: absolute;
    top: 196px;
    right: 48px;
    text-align: right;
    font-size: 12.5px;
    font-weight: 400;
    line-height: 1.25;
  }
  .front-services .services-label { margin-right: 110px; }

  /* Back (contact) side */
  .card-back {
    background: var(--white);
    color: var(--grey-text);
    border-top: 3px solid var(--orange);
  }
  .back-edge-right {
    position: absolute;
    top: 0; right: 0;
    width: 14px;
    height: 100%;
    background: linear-gradient(180deg, var(--orange-deep), var(--orange));
  }
  .back-edge-bottom {
    position: absolute;
    left: 0; right: 0; bottom: 0;
    height: 22px;
    background: linear-gradient(90deg, var(--yellow) 0%, var(--amber) 45%, var(--orange) 100%);
  }
  .back-brand {
    position: absolute;
    top: 28px;
    left: 30px;
  }
  .back-brand .brand-name { color: var(--orange); font-size: 56px; }
  .back-brand .brand-tagline { color: var(--grey-text); font-size: 15px; margin-left: 34px; }
  .contact-person {
    position: absolute;
    top: 160px;
    left: 30px;
  }
  .person-name {
    color: var(--orange);
    font-weight: 400;
    font-size: 27px;
    line-height: 1.1;
  }
  .person-role {
    font-size: 13.5px;
    margin-top: 4px;
    margin-bottom: 8px;
  }
  .contact-line {
    display: flex;
    align-items: center;
    gap: 6px;
    font-size: 14px;
    line-height: 1.3;
  }
  .contact-line svg { width: 11px; height: 11px; flex: none; }
  .contact-address {
    position: absolute;
    top: 168px;
    left: 300px;
    font-size: 13px;
    line-height: 1.25;
    font-style: normal;
  }
</style>
</head>
<body>

  <section class="card card-front" aria-label="Business card front">
    <div class="front-band"></div>
    <div class="front-watermark upper" aria-hidden="true">kestrel</div>
    <div class="front-watermark lower" aria-hidden="true">kestrel</div>
    <div class="front-brand">
      <div class="brand-name">kestrel</div>
      <div class="brand-tagline">communications pty ltd</div>
    </div>
    <div class="front-services">
      <div class="services-label">services:</div>
      <div>cabling / data / phone / antennas / audio visual</div>
      <div>home theatre / fibre optics</div>
    </div>
  </section>

  <section class="card card-back" aria-label="Business card back">
    <div class="back-edge-right"></div>
    <div class="back-edge-bottom"></div>
    <div class="back-brand">
      <div class="brand-name">kestrel</div>
      <div class="brand-tagline">communications pty ltd</div>
    </div>
    <div class="contact-person">
      <div class="person-name">Doug Pemberton</div>
      <div class="person-role">Director/Technician</div>
      <div class="contact-line">
        <svg viewBox="0 0 12 12" aria-hidden="true"><path d="M3 1 L5 3.5 L4 5 Q5 7 7 8 L8.5 7 L11 9 L9.5 11 Q4 10.5 1 3 Z" fill="var(--orange)"/></svg>
        <span>0437196084</span>
      </div>
      <div class="contact-line">
        <svg viewBox="0 0 12 12" aria-hidden="true"><rect x="1" y="2.5" width="10" height="7" fill="none" stroke="var(--orange)" stroke-width="1.3"/><path d="M1 2.5 L6 6.5 L11 2.5" fill="none" stroke="var(--orange)" stroke-width="1.3"/></svg>
        <span>kestrel4me@maildrop-example.com</span>
      </div>
    </div>
    <address class="contact-address">
      PO BOX 657 Marlow Flats<br>
      QLD 4873 Australia
    </address>
  </section>

</body>
</html>
```